7QK Pop Up Shop Clearance Flyer

We sell furniture. We opened up recently a temporary pop up shop to clear some stock we had from our old shop. So we don't have a full collection just our clearance lines that we want to get rid of - but the customer doesn't need to know this! Therefore the aim of this leaflet is to attract customers and make them come in - once they are there they might see something they like. As we will not be there for long - just a few more weeks.
We need a flyer to promote locally our pop up shop (temporary shop) with a Clearance Sale. The flyer will be sent by post or by hand to the local residents and by email to ex customers that bought from us before and we have their email address...
We need a modern fresh design flyer. At the next stage we will provide text for each item (brief description, dimensions and price) so allow some space for this.
Maybe we need to add a message or something to make people want to come quickly? For example most of the items are ex display or the last item and if they want it they should hurry as one is gone its gone. or you may have a better suggestion - let me know.
if you want to see some ideas of our website then 7QK.co.uk

Target Market(s)

Local Residents around shop

Industry/Entity Type

Retail

Colors
0255a3
3176b5
85abd2

Requirements
Must have
• price tag showing RRP or WAS price and the Clearance Sale price
• Opening Hours: Mon-Fri 9:00am - 5:00pm, Sat: 9:00am - 4:00pm, Sun: Closed
• Tel: 0208 915 2730
• Shop Address: 184 Birch Rowe, Elmwick Vale, London, N21 7PD
Nice to have
• Parking behind Bo Tarvins
• Map of location

```html
<!DOCTYPE html>
<html lang="en">
<head>
<meta charset="utf-8">
<title>7QK Clearance Sale Flyer</title>
<link rel="stylesheet" href="https://fonts.googleapis.com/css2?family=Rubik:wght@800&family=Lato:wght@400;700;900&display=swap">
<style>
  :root {
    --blue-deep: #0255a3;
    --blue-mid: #3176b5;
    --blue-soft: #85abd2;
    --tag-navy: #1d3f7c;
    --grey-text: #6a6a6a;
    --grey-panel: #dcdcdc;
    --ink: #3a3a3a;
    --paper: #ffffff;
    --backdrop: #ececec;
  }
  * { box-sizing: border-box; margin: 0; padding: 0; }
  html, body { width: 1112px; height: 1200px; overflow: hidden; background: var(--backdrop); }
  .flyer {
    position: absolute; left: 138px; top: 10px;
    width: 836px; height: 1180px;
    background: var(--paper);
    font-family: "Lato", sans-serif;
  }
  .headline {
    position: absolute; top: 62px; left: 0; width: 100%;
    text-align: center;
    font-family: "Rubik", sans-serif; font-weight: 800;
    font-size: 82px; letter-spacing: 1px; line-height: 1;
    color: var(--blue-deep);
  }
  .subhead {
    position: absolute; top: 155px; left: 0; width: 100%;
    text-align: center; font-weight: 700; font-size: 30px; line-height: 38px;
    color: var(--grey-text); text-transform: uppercase;
  }
  .photo { position: absolute; overflow: hidden; }
  .photo--bedroom {
    left: 24px; top: 262px; width: 788px; height: 332px;
    background: linear-gradient(172deg,
      #f3f4f3 0%, #e6e7e5 30%, #bfbcb6 46%, #5e5249 58%,
      #e8e7e4 66%, #a9a6a1 74%, #6a5a4d 84%, #c9775a 94%, #b46a52 100%);
  }
  .photo--lounger {
    left: 24px; top: 616px; width: 374px; height: 222px;
    background: linear-gradient(178deg,
      #f6f6f4 0%, #ececea 45%, #cfc8c0 62%, #8f8073 72%, #e3e0dc 84%, #d6d2cc 100%);
  }
  .photo--armchair {
    left: 426px; top: 622px; width: 378px; height: 222px;
    background: linear-gradient(100deg,
      #c6a992 0%, #b5452f 18%, #d2a04a 34%, #c98a30 52%, #8e5a3a 66%,
      #e4ddd4 78%, #cfc6bb 100%);
  }
  .price-tag { position: absolute; transform: rotate(-9deg); transform-origin: left top; }
  .price-tag__band {
    display: block; background: var(--tag-navy); opacity: 0.93;
    color: #fff; font-weight: 700; white-space: nowrap;
    margin-bottom: 5px;
  }
  .price-tag--large { left: 566px; top: 198px; }
  .price-tag--large .price-tag__band { font-size: 19px; padding: 8px 80px 8px 20px; }
  .price-tag--large .price-tag__band--now { font-size: 25px; }
  .price-tag--small .price-tag__band { font-size: 14px; padding: 5px 60px 5px 14px; margin-bottom: 4px; }
  .price-tag--small .price-tag__band--now { font-size: 18px; }
  .price-tag--left { left: -6px; top: 38px; }
  .price-tag--left .price-tag__band { padding-right: 20px; }
  .price-tag--right { left: 230px; top: 64px; }
  .hours {
    position: absolute; left: 14px; top: 862px; width: 278px; height: 292px;
    background: var(--blue-soft); color: var(--blue-deep);
    text-align: center; font-weight: 700; font-size: 20px; line-height: 25px;
    padding-top: 22px;
  }
  .hours__title { padding-bottom: 6px; }
  .hours__rule { width: 150px; height: 2px; background: var(--blue-deep); margin: 0 auto 16px; }
  .hours__rule--after { margin: 14px auto 12px; }
  .contact {
    position: absolute; left: 318px; top: 868px; width: 504px; height: 292px;
    background: var(--grey-panel); padding: 42px 26px 0 26px;
  }
  .brand { display: flex; align-items: center; justify-content: flex-end; gap: 14px; margin-bottom: 26px; }
  .brand__mark { width: 40px; height: 40px; background: var(--blue-mid); }
  .brand__text { text-align: left; }
  .brand__name { font-size: 32px; font-weight: 400; color: var(--ink); letter-spacing: 0.5px; line-height: 1; }
  .brand__tagline { font-size: 16px; color: var(--ink); letter-spacing: 0.5px; margin-top: 4px; }
  .contact__tel { font-size: 46px; font-weight: 900; color: var(--blue-deep); line-height: 1; margin-bottom: 20px; }
  .contact__address { font-size: 24px; color: var(--ink); line-height: 33px; }
</style>
</head>
<body>
<main class="flyer">
  <h1 class="headline">CLEARANCE SALE</h1>
  <p class="subhead">For all types of furnitures supplied<br>from basic to luxury</p>

  <div class="photo photo--bedroom" role="img" aria-label="Photo of a bedroom with a dark wood bed, striped bedding, bedside tables, lamps and a dresser with mirror on an orange rug">
    <div class="price-tag price-tag--large">
      <span class="price-tag__band">RRP $ 00.00</span>
      <span class="price-tag__band">WAS $ 00.00</span>
      <span class="price-tag__band price-tag__band--now">NOW $ 00.00</span>
    </div>
  </div>

  <div class="photo photo--lounger" role="img" aria-label="Photo of a modern chaise lounger and sculptural side table in a bright white room with a potted plant">
    <div class="price-tag price-tag--small price-tag--left">
      <span class="price-tag__band">RRP $ 00.00</span>
      <span class="price-tag__band">WAS $ 00.00</span>
      <span class="price-tag__band price-tag__band--now">NOW $ 00.00</span>
    </div>
  </div>

  <div class="photo photo--armchair" role="img" aria-label="Photo of a mustard yellow wingback armchair beside a red vase and a small round side table">
    <div class="price-tag price-tag--small price-tag--right">
      <span class="price-tag__band">RRP $ 00.00</span>
      <span class="price-tag__band">WAS $ 00.00</span>
      <span class="price-tag__band price-tag__band--now">NOW $ 00.00</span>
    </div>
  </div>

  <section class="hours">
    <div class="hours__title">Opening Hours:</div>
    <div class="hours__rule"></div>
    <div>Monday to Friday</div>
    <div>9:00am-5:00pm</div>
    <div>Saturday</div>
    <div>9:00am-4:00pm</div>
    <div>Sunday: Closed</div>
    <div class="hours__rule hours__rule--after"></div>
    <div>Parking</div>
    <div>behind Bo Tarvins</div>
  </section>

  <section class="contact">
    <div class="brand">
      <span class="brand__mark"></span>
      <div class="brand__text">
        <div class="brand__name">7QK FURNITURE</div>
        <div class="brand__tagline">TRADE FURNITURE SOLUTIONS</div>
      </div>
    </div>
    <div class="contact__tel">Tel: 0208 915 2730</div>
    <p class="contact__address">Shop Address: 184 Birch Rowe,<br>Elmwick Vale, London, N21 7PD</p>
  </section>
</main>
</body>
</html>
```